Stationery for Villa Marejada Design Hotel**

Who we are:

Wander on an isolated beach while breathing in the fresh, salty, sea air. Listen to the warm Pacific wind rustling through green palm trees as you walk to a pristine lagoon. Feel the delicious warmth of the sun kiss your skin; the beach is yours. At Villa Marejada you can experience a vacation in undisturbed, natural beauty. We have created a place for you to find new strength, relaxation, and inner harmony. We offer total rest to the experienced traveler from all over the world.

We are a brand new and smartly built design-hotel (under construction) close to a unique beach and a fantastic surf spot in Huatulco, Southwest Mexico.

As you can see in the attachments, we do have an established corporate design, but as for now still need a format for booklets for information around our hotel and things to do in the area, important numbers (we fill in the content for that one).

Our corporate colors:
green #64b445, brown #b07043, blue #0ab7cf, yellow # f9b02a and #fcc01a, navy #444f69
Corporate fonts:
Krub and Miller Banner.
For further information access:
www.villamarejada.example
https://slideshare.example/view/QxLmPwTr8KdNvYsZhJcA/

Social Media: VillaMarejada

Industry/Entity Type

Hotel

Font styles to use
Other font styles liked:
• Krub, Miller Banner

Requirements
Must have
• Stick to Logo Design, defined corporate elements, logo, colors, fonts and general touch and feel
Nice to have
• Who we are:

Our corporate colors:
Corporate fonts:
Krub and Miller Banner.
www.villamarejada.example

Social Media: VillaMarejada

```html
<!DOCTYPE html>
<html lang="en">
<head>
<meta charset="utf-8">
<title>Villa Marejada – Letterhead</title>
<link href="https://fonts.googleapis.com/css2?family=Krub:wght@400;500;600&display=swap" rel="stylesheet">
<style>
  :root {
    --backdrop: #dde2e2;
    --paper: #ffffff;
    --gold: #e0a21c;
    --gold-bar: #f0a81e;
    --teal: #167f8c;
    --grey-text: #6f6f6f;
    --rule: #9a9a9a;
    --swoosh-green: #e8f2dc;
    --swoosh-blue: #dbeff2;
    --leaf: #e6f0da;
  }
  * { box-sizing: border-box; margin: 0; padding: 0; }
  html, body {
    width: 1200px; height: 784px; overflow: hidden;
    background: var(--backdrop);
  }
  .canvas {
    position: relative; width: 1200px; height: 784px;
    display: flex; align-items: center; justify-content: center;
  }
  .letterhead {
    position: relative; width: 520px; height: 735px;
    background: var(--paper);
    overflow: hidden;
    box-shadow: 0 2px 10px rgba(0,0,0,0.08);
  }
  .swooshes { position: absolute; inset: 0; width: 100%; height: 100%; }
  .brand {
    position: absolute; top: 34px; left: 34px;
  }
  .brand-name {
    font-family: "Krub", sans-serif; font-weight: 600;
    font-size: 20px; letter-spacing: 1px; color: var(--gold);
    text-transform: uppercase;
  }
  .leaf-decoration {
    position: absolute; right: 40px; bottom: -30px;
    width: 200px; height: 190px; border-radius: 50% 50% 45% 45%;
    background: radial-gradient(circle at 50% 45%, var(--leaf), rgba(230,240,218,0.5));
  }
  .footer {
    position: absolute; left: 24px; width: 330px; bottom: 20px;
    display: flex; flex-direction: column; align-items: center; gap: 5px;
    font-family: "Krub", sans-serif;
  }
  .icon-row { display: flex; align-items: center; gap: 8px; margin-bottom: 4px; }
  .icon-row .rule { width: 48px; height: 1px; background: var(--rule); }
  .icon {
    width: 13px; height: 13px; border-radius: 50%; background: var(--gold);
    display: flex; align-items: center; justify-content: center;
  }
  .icon svg { width: 9px; height: 9px; }
  .address { font-size: 10.5px; color: var(--teal); letter-spacing: 0.2px; white-space: nowrap; }
  .contact { font-size: 9.5px; color: var(--grey-text); white-space: nowrap; }
  .gold-bar {
    position: absolute; left: 0; right: 0; bottom: 0; height: 6px;
    background: var(--gold-bar);
  }
</style>
</head>
<body>
<div class="canvas">
  <section class="letterhead">
    <svg class="swooshes" viewBox="0 0 520 735" preserveAspectRatio="none" aria-hidden="true">
      <path d="M0 72 Q 260 150 520 300 L 520 322 Q 250 168 0 86 Z" fill="var(--swoosh-green)"/>
      <path d="M330 222 Q 440 262 520 318 L 520 330 Q 430 278 330 222 Z" fill="var(--swoosh-blue)"/>
    </svg>

    <div class="brand">
      <span class="brand-name">Villa Marejada</span>
    </div>

    <div class="leaf-decoration" role="img" aria-label="Faint watercolour monstera leaf decoration"></div>

    <footer class="footer">
      <div class="icon-row">
        <span class="rule"></span>
        <span class="icon"><svg viewBox="0 0 10 10"><path d="M5 1a3 3 0 0 1 3 3c0 2-3 5-3 5S2 6 2 4a3 3 0 0 1 3-3z" fill="#fff"/></svg></span>
        <span class="icon"><svg viewBox="0 0 10 10"><path d="M2.5 1.5l1.5 1.5-1 1c.6 1.2 1.4 2 2.6 2.6l1-1 1.5 1.5-1 1C4.5 8 2 5.5 1.5 2.5z" fill="#fff"/></svg></span>
        <span class="icon"><svg viewBox="0 0 10 10"><circle cx="5" cy="5" r="3" fill="none" stroke="#fff" stroke-width="1.2"/></svg></span>
        <span class="icon"><svg viewBox="0 0 10 10"><rect x="1.5" y="2.5" width="7" height="5" fill="none" stroke="#fff"/><path d="M1.5 2.5l3.5 3 3.5-3" fill="none" stroke="#fff"/></svg></span>
        <span class="icon"><svg viewBox="0 0 10 10"><circle cx="5" cy="5" r="3.5" fill="none" stroke="#fff" stroke-width="0.9"/><path d="M1.5 5h7M5 1.5v7" stroke="#fff" stroke-width="0.8"/></svg></span>
        <span class="rule"></span>
      </div>
      <p class="address">Villa Marejada, Playa Serena, Costa Linda, Oaxaca, Mexico</p>
      <p class="contact">+52 1 (958) 555 0142 | hello@villamarejada.example | www.villamarejada.example</p>
    </footer>

    <div class="gold-bar"></div>
  </section>
</div>
</body>
</html>
```